Security Warning Sign

We have an existing sign that needs an update. I have attached a picture of the current square sign. We need to maintain the same wording. It needs to be professional and appropriate to attach to our customers fence. Also attached is a copy of our building sign which may lend some inspiration and hopefully the ai format will assist. The final sign will be 600mm x 600mmOur website is www.halvorngate.com.au

```html
<!DOCTYPE html>
<html lang="en">
<head>
<meta charset="utf-8">
<title>Security Warning Sign – Halvorngate Security</title>
<link rel="stylesheet" href="https://fonts.googleapis.com/css2?family=Anton&family=Roboto+Condensed:wght@700;800&display=swap">
<style>
  :root {
    --frame-silver: #c9cccd;
    --sign-black: #1c1a19;
    --warning-orange: #f3951f;
    --panel-white: #ffffff;
    --ink-black: #161413;
    --camera-tone: #d9d9d9;
  }
  html, body {
    margin: 0;
    padding: 0;
    width: 1200px;
    height: 1200px;
    overflow: hidden;
    background: #ffffff;
  }
  .sign {
    display: block;
    width: 1200px;
    height: 1200px;
  }
  .warning-title {
    font-family: "Anton", "Roboto Condensed", sans-serif;
    font-size: 142px;
    fill: var(--ink-black);
  }
  .notice-line {
    font-family: "Roboto Condensed", "Arial Narrow", sans-serif;
    font-weight: 800;
    font-size: 124px;
    fill: var(--ink-black);
    text-anchor: middle;
  }
  .company-tagline {
    font-family: "Roboto Condensed", "Arial Narrow", sans-serif;
    font-weight: 800;
    font-size: 40px;
    letter-spacing: 3px;
    fill: var(--panel-white);
    text-anchor: end;
  }
  .company-name {
    font-family: "Roboto Condensed", "Arial Narrow", sans-serif;
    font-weight: 800;
    font-size: 112px;
    fill: var(--panel-white);
  }
  .phone-number {
    font-family: "Roboto Condensed", "Arial Narrow", sans-serif;
    font-weight: 800;
    font-size: 74px;
    fill: var(--ink-black);
  }
</style>
</head>
<body>
<svg class="sign" viewBox="0 0 1200 1200" xmlns="http://www.w3.org/2000/svg">
  <!-- metal frame -->
  <rect class="sign-frame" x="0" y="0" width="1200" height="1200" rx="34" fill="var(--frame-silver)"/>
  <!-- black sign face -->
  <rect class="sign-face" x="38" y="38" width="1124" height="1124" rx="34" fill="var(--sign-black)"/>

  <!-- warning banner -->
  <polygon class="warning-banner" points="70,60 858,60 938,222 70,222" fill="var(--warning-orange)"/>
  <text class="warning-title" x="84" y="203" textLength="742" lengthAdjust="spacingAndGlyphs">WARNING</text>

  <!-- camera icon area -->
  <rect class="camera-icon" x="928" y="70" width="196" height="150" rx="12" fill="var(--camera-tone)"
        role="img" aria-label="Security camera icon"/>

  <!-- notice panel -->
  <rect class="notice-panel" x="74" y="246" width="1052" height="718" fill="var(--panel-white)"/>
  <text class="notice-line" x="600" y="373">ELECTRONIC</text>
  <text class="notice-line" x="600" y="508">SURVEILLANCE</text>
  <text class="notice-line" x="600" y="644">AND RECORDING</text>
  <text class="notice-line" x="600" y="779">DEVICE INSTALLED</text>
  <text class="notice-line" x="600" y="915">IN THIS AREA</text>

  <!-- company name -->
  <circle class="company-mark" cx="160" cy="1086" r="40" fill="var(--warning-orange)"/>
  <text class="company-name" x="226" y="1128">HGS</text>

  <text class="company-tagline" x="1124" y="1030">HALVORNGATE SECURITY</text>

  <!-- phone band -->
  <polygon class="phone-band" points="482,1046 1126,1046 1126,1136 440,1136" fill="var(--warning-orange)"/>
  <g class="phone-icon" transform="translate(492 1064) rotate(-20 26 28)">
    <path d="M13 4 C7 4 4 9 5 16 C9 31 22 46 37 52 C45 54 50 50 50 45 L50 39 L39 34 L34 39 C26 35 21 30 17 22 L22 17 L17 4 Z"
          fill="var(--ink-black)"/>
  </g>
  <text class="phone-number" x="578" y="1117" textLength="527" lengthAdjust="spacing">1300 555 014</text>
</svg>
</body>
</html>
```